Design for LED christmas lights

📦 Packaging Briefing – Christmas Lights (Glowna)
First design for approval – Product: 360 LED Warm White String Lights – Connectable, 8 Functions, IP44, EU Plug
🧩 Project Overview:
We are developing 6 unique box styles for the Glowna Christmas lighting range, covering 11 design variations (e.g. LED counts, lengths, plug types). This briefing is for the initial box design to be created for internal approval, based on the yellow-highlighted product in the provided Excel file.
✅ Design Style:
Use the same layout, typography, and structure as the attached LED bulb box.
The font and overall style must remain consistent with that example.
Only adjust layout elements as needed to accommodate Christmas light visuals and product-specific features.
📌 Box Content (for this product):
Product Name (front and sides):
360 LED Warm White String Lights – Connectable, 8 Functions, IP44, EU Plug
Highlight these features (icons or bullet format):
360 LEDs
Warm White
Connectable
8 Functions
IP44 (outdoor suitable)
EU Plug
Also include:
CE logo
EAN barcode (from Excel file)
Article number (from Excel file)
🖼 Visuals:
Use the corresponding product image from the Excel file.
Integrate image into the layout similarly to how the LED bulb is shown on its box (clean placement, no background clutter).
🏷 Brand & Company Info:
Brand/logo: Glowna (see attached logo file)
Company name: Brisk Harbor B.V.
Email: info@vonkelhuis.nl
Phone: +31 487 5914
🎨 Tone & Feel:
Clean, professional, and slightly festive – think minimal Christmas warmth, not overly decorative
Style should match the LED bulb box to build a coherent product line

```html
<!DOCTYPE html>
<html lang="en">
<head>
<meta charset="utf-8">
<title>Glowna – 360 LED Warm White String Lights – Box Dieline</title>
<link href="https://fonts.googleapis.com/css2?family=Montserrat:wght@300;400;600;700&display=swap" rel="stylesheet">
<style>
  :root {
    --bg: #f1f1f1;
    --charcoal: #363636;
    --charcoal-soft: #404040;
    --orange: #f4a024;
    --orange-deep: #f08a3a;
    --white: #ffffff;
    --ink: #2e2e2e;
    --fold: #5a5a5a;
  }
  html, body {
    margin: 0;
    width: 918px;
    height: 1200px;
    overflow: hidden;
    background: var(--bg);
    font-family: "Montserrat", sans-serif;
  }
  .canvas {
    width: 918px;
    height: 1200px;
    display: flex;
    align-items: center;
    justify-content: center;
  }
  .dieline { display: block; }
  .fill-dark { fill: var(--charcoal); }
  .fill-dark-soft { fill: var(--charcoal-soft); }
  .fill-orange { fill: var(--orange); }
  .t { font-family: "Montserrat", sans-serif; }
  .t-light { font-weight: 300; }
  .t-reg { font-weight: 400; }
  .t-semi { font-weight: 600; }
  .t-bold { font-weight: 700; }
  .c-white { fill: var(--white); }
  .c-orange { fill: var(--orange); }
  .c-ink { fill: var(--ink); }
  .brand { letter-spacing: 4px; }
</style>
</head>
<body>
<main class="canvas">
<svg class="dieline" width="880" height="416" viewBox="90 155 1460 690" xmlns="http://www.w3.org/2000/svg">
  <defs>
    <linearGradient id="front-glow" x1="0" y1="0" x2="0" y2="1">
      <stop offset="0" stop-color="#f0903e"/>
      <stop offset="0.45" stop-color="#c88a3a"/>
      <stop offset="1" stop-color="#474241"/>
    </linearGradient>
    <linearGradient id="photo-tone" x1="0" y1="0" x2="1" y2="1">
      <stop offset="0" stop-color="#c98a45" stop-opacity="0.6"/>
      <stop offset="0.5" stop-color="#8a5533"/>
      <stop offset="1" stop-color="#5b3a2a"/>
    </linearGradient>
  </defs>

  <!-- top tuck flap + top panel -->
  <g class="top-panel">
    <path class="fill-dark-soft" d="M145 205 V180 Q145 160 170 160 H580 Q600 160 600 180 V205 Z"/>
    <rect class="fill-dark-soft" x="138" y="203" width="469" height="238"/>
    <line x1="370" y1="203" x2="420" y2="203" stroke="var(--fold)" stroke-width="1.5"/>
    <g transform="rotate(180 372.5 300.5)">
      <text class="t t-light c-orange" x="193" y="206" font-size="22">STRING LIGHTS</text>
      <text class="t t-reg c-white" x="378" y="206" font-size="15">360 LED Warm White</text>
      <rect class="fill-orange" x="323" y="223" width="104" height="24" rx="4"/>
      <text class="t t-semi c-white" x="375" y="240" font-size="12" text-anchor="middle">Connectable</text>
      <rect class="fill-orange" x="449" y="223" width="104" height="24" rx="4"/>
      <text class="t t-semi c-white" x="501" y="240" font-size="12" text-anchor="middle">8 Functions</text>
      <text class="t t-light c-orange brand" x="195" y="282" font-size="18">GLOWNA</text>
      <text class="t t-reg c-white" x="193" y="304" font-size="10">Brisk Harbor B.V.</text>
      <text class="t t-reg c-white" x="193" y="318" font-size="10">Email: info@vonkelhuis.nl</text>
      <text class="t t-reg c-white" x="193" y="332" font-size="10">Phone: +31 487 5914</text>
      <g class="feature-bullets">
        <circle class="c-orange" cx="388" cy="281" r="1.8"/><text class="t c-white" x="394" y="284" font-size="7.5">360 LEDs</text>
        <circle class="c-orange" cx="388" cy="291" r="1.8"/><text class="t c-white" x="394" y="294" font-size="7.5">Warm White</text>
        <circle class="c-orange" cx="388" cy="301" r="1.8"/><text class="t c-white" x="394" y="304" font-size="7.5">8 Functions</text>
        <circle class="c-orange" cx="388" cy="311" r="1.8"/><text class="t c-white" x="394" y="314" font-size="7.5">Connectable</text>
        <circle class="c-orange" cx="388" cy="321" r="1.8"/><text class="t c-white" x="394" y="324" font-size="7.5">IP44 (outdoor suitable)</text>
        <circle class="c-orange" cx="388" cy="331" r="1.8"/><text class="t c-white" x="394" y="334" font-size="7.5">EU Plug</text>
      </g>
      <circle cx="526" cy="283" r="13" fill="none" stroke="var(--white)" stroke-width="3"/>
      <text class="t t-semi c-white" x="165" y="373" font-size="12">360 LED</text>
      <text class="t t-semi c-white" x="265" y="373" font-size="12">IP44</text>
      <text class="t t-semi c-white" x="330" y="373" font-size="12">EU Plug</text>
      <text class="t t-semi c-white" x="410" y="373" font-size="12">Connectable</text>
      <text class="t t-semi c-white" x="500" y="373" font-size="12">8 Functions</text>
    </g>
  </g>

  <!-- glue flap -->
  <polygon class="fill-orange" points="95,452 138,441 138,678 95,662"/>

  <!-- front panel -->
  <g class="front-panel">
    <rect x="138" y="441" width="469" height="187" fill="url(#front-glow)"/>
    <rect x="405" y="441" width="202" height="187" fill="url(#photo-tone)" role="img" aria-label="Photo of warm white icicle string lights with a white outlined Christmas tree"/>
    <text class="t t-reg c-white" x="168" y="480" font-size="28">360 LED Warm White</text>
    <text class="t t-reg c-white" x="168" y="518" font-size="38">STRING LIGHTS</text>
    <text class="t t-light c-white brand" x="175" y="568" font-size="22">GLOWNA</text>
    <rect class="fill-orange" x="172" y="582" width="104" height="24" rx="4"/>
    <text class="t t-semi c-white" x="224" y="599" font-size="13" text-anchor="middle">Connectable</text>
    <rect class="fill-orange" x="298" y="582" width="104" height="24" rx="4"/>
    <text class="t t-semi c-white" x="350" y="599" font-size="13" text-anchor="middle">8 Functions</text>
    <rect class="fill-orange" x="138" y="628" width="469" height="50"/>
    <text class="t t-semi c-ink" x="162" y="657" font-size="13.5">360 LED  |  IP44  |  EU Plug  |  Connectable  |  8 Functions</text>
  </g>
  <path class="fill-orange" d="M141 678 H604 V840 H492 V800 Q492 792 484 792 H262 Q254 792 254 800 V840 H141 Z"/>

  <!-- side panel 1 -->
  <g class="side-panel">
    <polygon class="fill-dark" points="616,337 820,337 838,441 607,441"/>
    <rect class="fill-dark" x="607" y="441" width="234" height="237"/>
    <path class="fill-dark" d="M612 678 H840 V840 H740 Q730 840 730 830 V797 Z"/>
    <text class="t t-light c-orange brand" x="727" y="497" font-size="32" text-anchor="middle">GLOWNA</text>
    <circle cx="727" cy="563" r="44" fill="#3d3a36" stroke="var(--orange)" stroke-width="1.5" role="img" aria-label="Line drawing of icicle string lights"/>
    <text class="t t-reg c-white" x="727" y="640" font-size="13" text-anchor="middle">360 LED Warm White</text>
    <text class="t t-light c-orange" x="727" y="660" font-size="20" text-anchor="middle">STRING LIGHTS</text>
  </g>

  <!-- back panel -->
  <g class="back-panel">
    <path class="fill-dark-soft" d="M1028 441 V408 Q1028 398 1038 398 H1110 Q1120 398 1120 408 V441 Z"/>
    <rect x="841" y="441" width="468" height="187" fill="url(#front-glow)"/>
    <rect x="1107" y="441" width="202" height="187" fill="url(#photo-tone)" role="img" aria-label="Photo of warm white icicle string lights with a white outlined Christmas tree"/>
    <text class="t t-reg c-white" x="870" y="480" font-size="28">360 LED Warm White</text>
    <text class="t t-reg c-white" x="870" y="518" font-size="38">STRING LIGHTS</text>
    <text class="t t-light c-white brand" x="877" y="568" font-size="22">GLOWNA</text>
    <rect class="fill-orange" x="874" y="582" width="104" height="24" rx="4"/>
    <text class="t t-semi c-white" x="926" y="599" font-size="13" text-anchor="middle">Connectable</text>
    <rect class="fill-orange" x="1000" y="582" width="104" height="24" rx="4"/>
    <text class="t t-semi c-white" x="1052" y="599" font-size="13" text-anchor="middle">8 Functions</text>
    <rect class="fill-orange" x="841" y="628" width="468" height="50"/>
    <text class="t t-semi c-ink" x="864" y="657" font-size="13.5">360 LED  |  IP44  |  EU Plug  |  Connectable  |  8 Functions</text>
  </g>
  <path class="fill-orange" d="M845 678 H1305 L1190 793 V830 Q1190 840 1180 840 H968 Q958 840 958 830 V793 Z"/>

  <!-- side panel 2 -->
  <g class="side-panel">
    <polygon class="fill-dark" points="1335,337 1532,337 1532,441 1315,441"/>
    <rect class="fill-dark" x="1309" y="441" width="236" height="237"/>
    <path class="fill-dark" d="M1312 678 H1535 L1422 790 V830 Q1422 840 1412 840 H1312 Z"/>
    <text class="t t-light c-orange brand" x="1428" y="497" font-size="32" text-anchor="middle">GLOWNA</text>
    <circle cx="1428" cy="563" r="44" fill="#3d3a36" stroke="var(--orange)" stroke-width="1.5" role="img" aria-label="Line drawing of icicle string lights"/>
    <text class="t t-reg c-white" x="1428" y="640" font-size="13" text-anchor="middle">360 LED Warm White</text>
    <text class="t t-light c-orange" x="1428" y="660" font-size="20" text-anchor="middle">STRING LIGHTS</text>
  </g>
</svg>
</main>
</body>
</html>
```